Two Bodyguards

Cover for a book in French language:
- Author: Mathieu Ferrand-Lacoste
- Title: Cold suspects rarely ever smile back
- Publisher (at the bottom of the page): Editions Vernaille
Key Words:
- a rich man died recently, it looks like a murder. He has been found in his luxury apartment.
- Two Body Guards: one is elegant, the other a bit fat.
- two pretty women.
- Inheritance (wealth)
Size of the cover: 14 x 20.5 cm (+ bleed area)
Please note that the title should remain in English: "Suspects rarely ever smile back".
By the way the title doesn't mean anything. It's just a joke.
Thrillers' reader

```html
<!DOCTYPE html>
<html lang="fr">
<head>
<meta charset="utf-8">
<title>Cold suspects rarely ever smile back — Mathieu Ferrand-Lacoste</title>
<link rel="stylesheet" href="https://fonts.googleapis.com/css2?family=Cinzel:wght@400&family=Marcellus&display=swap">
<style>
  :root {
    --stage: #1c1c1c;
    --paper: #f2f2f2;
    --paper-edge: #d6d6d6;
    --ink: #15171b;
    --rim: #5a1518;
    --note-gold: #d9b070;
    --note-red: #c0584a;
    --title: #ffffff;
    --author: #1a1a1a;
  }
  * { margin: 0; padding: 0; box-sizing: border-box; }
  html, body {
    width: 1200px;
    height: 926px;
    overflow: hidden;
    background: var(--stage);
  }
  .cover {
    position: absolute;
    left: 342px;
    top: 60px;
    width: 510px;
    height: 814px;
    background: var(--paper);
    overflow: hidden;
    box-shadow: 0 20px 60px rgba(0,0,0,0.6);
  }
  .cover-art {
    position: absolute;
    inset: 0;
    width: 510px;
    height: 814px;
  }
  .author {
    position: absolute;
    top: 34px;
    left: 0;
    width: 100%;
    text-align: center;
    font-family: 'Cinzel', serif;
    font-size: 26px;
    letter-spacing: 4px;
    color: var(--author);
    white-space: nowrap;
  }
  .title {
    position: absolute;
    top: 284px;
    left: 0;
    width: 100%;
    text-align: center;
    font-family: 'Cinzel', serif;
    font-weight: 400;
    color: var(--title);
    line-height: 1;
    text-transform: uppercase;
  }
  .title-line { display: block; white-space: nowrap; }
  .title-line--big { font-size: 92px; line-height: 0.88; }
  .title-line--wide { font-size: 74px; line-height: 1.02; }
  .title-line--small { font-size: 31px; margin-top: 4px; }
  .title-line--medium { font-size: 52px; line-height: 1.06; }
  .publisher {
    position: absolute;
    top: 756px;
    left: 0;
    width: 100%;
    text-align: center;
    font-family: 'Marcellus', serif;
    font-size: 27px;
    color: var(--title);
  }
</style>
</head>
<body>
  <main class="cover">
    <svg class="cover-art" viewBox="0 0 510 814">
      <defs>
        <radialGradient id="paper-texture" cx="50%" cy="30%" r="75%">
          <stop offset="0%" stop-color="#ffffff"/>
          <stop offset="60%" stop-color="#ededed"/>
          <stop offset="100%" stop-color="#d4d4d4"/>
        </radialGradient>
        <linearGradient id="figure-fill" x1="0" y1="0" x2="1" y2="0">
          <stop offset="0%" stop-color="#15171b"/>
          <stop offset="80%" stop-color="#1b1a1e"/>
          <stop offset="100%" stop-color="#3e1518"/>
        </linearGradient>
        <linearGradient id="note-fill" x1="0" y1="0" x2="1" y2="1">
          <stop offset="0%" stop-color="#e7c98c"/>
          <stop offset="100%" stop-color="#c49350"/>
        </linearGradient>
        <linearGradient id="note-fill-red" x1="0" y1="0" x2="1" y2="1">
          <stop offset="0%" stop-color="#eab4a0"/>
          <stop offset="100%" stop-color="#b5483c"/>
        </linearGradient>
        <linearGradient id="floor-shadow" x1="0" y1="0" x2="0" y2="1">
          <stop offset="0%" stop-color="#15171b" stop-opacity="0"/>
          <stop offset="100%" stop-color="#15171b" stop-opacity="0.9"/>
        </linearGradient>
      </defs>

      <rect class="paper" x="0" y="0" width="510" height="814" fill="url(#paper-texture)"/>
      <rect class="floor" x="0" y="720" width="510" height="94" fill="url(#floor-shadow)"/>

      <g class="figures" role="img" aria-label="Two bodyguards in dark silhouette, one slim and elegant in a long coat, one heavy-set">
        <rect class="figure figure--slim" x="34" y="128" width="200" height="612" rx="60" fill="url(#figure-fill)"/>
        <rect class="figure figure--heavy" x="222" y="80" width="278" height="726" rx="80" fill="url(#figure-fill)"/>
      </g>

      <g class="banknotes" role="img" aria-label="Euro banknotes falling around the two men">
        <rect x="4" y="130" width="70" height="40" fill="url(#note-fill-red)" transform="rotate(55 39 150)"/>
        <rect x="452" y="108" width="54" height="32" fill="url(#note-fill)" transform="rotate(-30 479 124)"/>
        <rect x="450" y="200" width="56" height="30" fill="url(#note-fill)" transform="rotate(-30 478 215)"/>
        <rect x="0" y="286" width="40" height="30" fill="url(#note-fill)" transform="rotate(-40 20 301)"/>
        <rect x="8" y="440" width="50" height="32" fill="url(#note-fill)" transform="rotate(55 33 456)"/>
        <rect x="444" y="468" width="56" height="38" fill="url(#note-fill)" transform="rotate(70 472 487)"/>
        <rect x="-6" y="558" width="44" height="30" fill="url(#note-fill)" transform="rotate(80 16 573)"/>
        <rect x="82" y="556" width="46" height="30" fill="url(#note-fill)" transform="rotate(80 105 571)"/>
        <rect x="30" y="612" width="54" height="28" fill="url(#note-fill-red)" transform="rotate(-60 57 626)"/>
        <rect x="390" y="596" width="66" height="38" fill="url(#note-fill)" transform="rotate(-60 423 615)"/>
        <rect x="450" y="634" width="58" height="32" fill="url(#note-fill-red)" transform="rotate(40 479 650)"/>
        <rect x="2" y="702" width="66" height="20" fill="url(#note-fill)" transform="rotate(12 35 712)"/>
        <rect x="476" y="746" width="36" height="12" fill="url(#note-fill-red)"/>
        <rect x="28" y="776" width="66" height="18" fill="url(#note-fill-red)" opacity="0.7"/>
        <rect x="360" y="788" width="42" height="22" fill="url(#note-fill-red)" opacity="0.6" transform="rotate(-25 381 799)"/>
      </g>
    </svg>

    <p class="author">Mathieu Ferrand-Lacoste</p>

    <h1 class="title">
      <span class="title-line title-line--big">Cold</span>
      <span class="title-line title-line--wide">Suspects</span>
      <span class="title-line title-line--small">Rarely ever</span>
      <span class="title-line title-line--medium">Smile back</span>
    </h1>

    <p class="publisher">Editions Vernaille</p>
  </main>
</body>
</html>
```